Outdoor group fitness training - Greta Pollock Personal Training

I want an eye catching A4 flyer that promotes my two outdoor fitness groups. I have uploaded photos of each location: Mylor and Pasadena.
The target group is existing and potential new Personal training clients - all adults. There are two morning groups at Mylor ; one evening and one morning group at Pasadena. The groups will be for up to 8 people and are for all fitness levels.I want to encourage people to come and have a go. I have also uploaded a design I have used through inkrally for a previous flyer. I would like to use the orange graphic of the two people at the bottom of this design.
Cost is $15 per person
Location and times - Brenton Green Wednesdays 7.30am; Sundays 8am
Kilvane High School Thursdays 6.30pm: Saturdays 8am
Updates

Thanks so much to all of you for submitting a great set of designs. it was really hard making a choice in the end, and I really appreciate the promptness and creativity that went into the designs. I will certainly keep you in mind for future jobs. Cheers and have a great day Greta Pollock

Target Market(s)

40 - 60 year old adults: cross section of professionals, tradespeople and retirees. People who will enjoy socialising while also getting fit. No extremely fit people - cross section of beginners to intermediate; males and females

Industry/Entity Type

Training

Font styles to use
Sans Serif

Colors
f78f20
9bcb3c
ecf7fb

Requirements
Must have
• Fast turnaround required - within two days
Bright and attention grabbing, engaging. Could be A4 or could be postcard size?

State cost clearly
State that first 5 people to join either group will get first session at half price

```html
<!DOCTYPE html>
<html lang="en">
<head>
<meta charset="utf-8">
<title>Greta Pollock Personal Training – Outdoor Group Fitness Flyer</title>
<link rel="stylesheet" href="https://fonts.googleapis.com/css2?family=Arimo:wght@700&family=Noto+Sans:wght@400&display=swap">
<style>
  :root {
    --lime: #8cef00;
    --orange: #f77f12;
    --pale: #f0fbfb;
    --red: #e8000b;
    --backdrop: #e9e6e1;
    --sepia-light: #d9b48c;
    --sepia-mid: #a8703f;
    --sepia-dark: #5e3a1d;
  }
  * { box-sizing: border-box; margin: 0; padding: 0; }
  html, body {
    width: 1200px;
    height: 982px;
    overflow: hidden;
    background: var(--backdrop);
  }
  .flyer {
    position: absolute;
    left: 282px;
    top: 41px;
    width: 636px;
    height: 900px;
    overflow: hidden;
    background: var(--lime);
    font-family: "Noto Sans", sans-serif;
    color: var(--orange);
    box-shadow: 0 4px 18px rgba(0,0,0,0.18);
  }
  .flyer__art {
    position: absolute;
    inset: 0;
    width: 636px;
    height: 900px;
  }
  .brand {
    position: absolute;
    left: 22px;
    top: 22px;
    font-family: "Arimo", sans-serif;
    font-weight: 700;
    font-size: 25px;
    color: var(--orange);
  }
  .offer {
    position: absolute;
    left: 100px;
    top: 150px;
    width: 250px;
    text-align: center;
    font-size: 27px;
    line-height: 1.2;
  }
  .offer__number { color: var(--lime); }
  .offer__highlight { color: var(--red); }
  .features {
    position: absolute;
    right: 34px;
    top: 138px;
    width: 250px;
    text-align: right;
    font-size: 20px;
    line-height: 1.2;
  }
  .features p { margin-bottom: 26px; }
  .cost {
    position: absolute;
    left: 96px;
    top: 362px;
    font-size: 25px;
    color: var(--lime);
  }
  .schedule-title {
    position: absolute;
    left: 98px;
    top: 410px;
    font-size: 20px;
  }
  .venue {
    position: absolute;
    font-size: 15px;
    line-height: 1.35;
  }
  .venue--green { left: 102px; top: 462px; }
  .venue--school { left: 110px; top: 548px; }
</style>
</head>
<body>
  <article class="flyer">
    <svg class="flyer__art" viewBox="0 0 636 900">
      <defs>
        <linearGradient id="runnersTone" x1="0" y1="0" x2="1" y2="1">
          <stop offset="0" stop-color="#a8703f"/>
          <stop offset="0.5" stop-color="#d9b48c"/>
          <stop offset="1" stop-color="#5e3a1d"/>
        </linearGradient>
      </defs>
      <rect class="runners-photo" x="0" y="470" width="636" height="430" fill="url(#runnersTone)"
            role="img" aria-label="Sepia photo of two people jogging along a waterside path"/>
      <path class="lime-wave" d="M0 0 H636 V505 C 460 560 250 640 0 720 Z" fill="var(--lime)"/>
      <path class="orange-arc" d="M14 662 C -30 400 14 95 245 35 C 400 -8 560 0 636 22 V 460 C 460 532 260 604 14 662 Z" fill="var(--orange)"/>
      <path class="info-panel" d="M40 644 C 0 400 40 125 262 62 C 400 24 560 28 636 52 V 470 C 460 540 262 612 40 644 Z" fill="var(--pale)"/>
      <path class="top-ribbon" d="M262 58 C 400 12 540 6 636 14" fill="none" stroke="var(--pale)" stroke-width="6"/>
    </svg>

    <div class="brand">Greta Pollock</div>

    <p class="offer">First <span class="offer__number">5</span> people to<br>join either group<br>will get first<br>session at<br><span class="offer__highlight">half price!</span></p>

    <div class="features">
      <p>Up to 8 people per<br>group.</p>
      <p>Beginners to<br>intermediate.</p>
      <p>Males and Females<br>are all welcome!</p>
      <p>Enjoy socialising<br>while getting fit at<br>the same time</p>
    </div>

    <p class="cost">Cost is $15 per person</p>
    <p class="schedule-title">Location and time:</p>
    <p class="venue venue--green">Brenton Green<br>Wednesdays 7.30am<br>Sundays 8am</p>
    <p class="venue venue--school">Kilvane High School<br>Thursdays 6.30pm Saturdays 8am</p>
  </article>
</body>
</html>
```